washable paper bags and accessories

We are three sisters who have discovered a mutual love of bags made from washable paper. It is a brand new business venture for bags, handbags, cosmetic bags, and home storage solutions and décor all made with washable paper.
We would like to have white crumpled paper as a background for both sides. Front of card with the words "plume douce cloth" only in "bohemian typewriter regular" font. Back of card with appointment style format for our next pop up stall
Target Market(s)
mums, females
Industry/Entity Type
Business
Contact Information for Business Card
ph: 0487215364
email:plumedoucecloth@mailbarrow.com

```html
<!DOCTYPE html>
<html lang="en">
<head>
<meta charset="UTF-8">
<title>plume douce cloth — business card front</title>
<link rel="stylesheet" href="https://fonts.googleapis.com/css2?family=Courier+Prime:wght@400&display=swap">
<style>
  :root {
    --paper-light: #f1f1f1;
    --paper-mid: #d9d9d9;
    --paper-shade: #b4b4b4;
    --paper-deep: #8e8e8e;
    --ink: #111111;
  }
  * { margin: 0; padding: 0; box-sizing: border-box; }
  html, body {
    width: 1200px;
    height: 700px;
    overflow: hidden;
    background: var(--paper-mid);
  }
  .card-front {
    position: relative;
    width: 1200px;
    height: 700px;
    overflow: hidden;
  }
  .crumpled-paper {
    position: absolute;
    inset: 0;
    background:
      radial-gradient(ellipse 60% 55% at 35% 18%, var(--paper-light) 0%, rgba(241,241,241,0) 70%),
      radial-gradient(ellipse 55% 60% at 85% 30%, #e6e6e6 0%, rgba(230,230,230,0) 70%),
      radial-gradient(ellipse 50% 55% at 0% 100%, var(--paper-deep) 0%, rgba(142,142,142,0) 70%),
      radial-gradient(ellipse 40% 50% at 100% 95%, var(--paper-shade) 0%, rgba(180,180,180,0) 70%),
      linear-gradient(160deg, #cfcfcf 0%, var(--paper-mid) 45%, #c4c4c4 100%);
  }
  .brand-name {
    position: absolute;
    left: 0;
    right: 0;
    top: 290px;
    text-align: center;
    font-family: "Courier Prime", "Courier New", monospace;
    font-weight: 400;
    font-size: 92px;
    line-height: 1;
    letter-spacing: 0;
    color: var(--ink);
    white-space: nowrap;
  }
</style>
</head>
<body>
  <main class="card-front">
    <div class="crumpled-paper" role="img" aria-label="White crumpled paper texture"></div>
    <h1 class="brand-name">plume douce cloth</h1>
  </main>
</body>
</html>
```